BrightHarbor, LLC
BrightHarbor
Creative Brief
Professional
Joan Ferris
Executive & Clinical Director
7183 Marbrook Avenue St. Louis, MO 63902
jferris@brightharborcare.example
www.brightharborcare.example
Card # 2 Nora Whitfield Marketing & Operations Director 7183 Marbrook Avenue St. Louis, MO 63902 Office Tel: 314-555-0172 Cell Tel: 314-555-0198 nwhitfield42@brightharborcare.example www.brightharborcare.example
WE APPRECIATE REFERRALS

```html
<!DOCTYPE html>
<html lang="en">
<head>
<meta charset="utf-8">
<title>BrightHarbor, LLC – Business Card</title>
<link href="https://fonts.googleapis.com/css2?family=Arimo:wght@400;700&display=swap" rel="stylesheet">
<style>
  :root {
    --backdrop: #d9dcdf;
    --card: #f4f4f2;
    --orange: #f39a1e;
    --navy: #2f3a4e;
    --ink: #3b3f45;
  }
  html, body {
    margin: 0;
    width: 1200px;
    height: 826px;
    overflow: hidden;
    background: var(--backdrop);
    font-family: "Arimo", Arial, sans-serif;
  }
  .card {
    position: absolute;
    left: 150px;
    top: 156px;
    width: 900px;
    height: 514px;
    background: var(--card);
    box-shadow: 0 10px 30px rgba(0,0,0,0.18);
    overflow: hidden;
  }
  .top-band {
    position: absolute;
    top: 0; left: 0; right: 0;
    height: 10px;
    display: flex;
  }
  .top-band .accent { flex: 0 0 52%; background: var(--orange); }
  .top-band .base { flex: 1; background: var(--navy); }

  .contact {
    position: absolute;
    left: 58px;
    top: 150px;
    color: var(--ink);
  }
  .contact .name {
    color: var(--orange);
    font-weight: 700;
    font-size: 26px;
    margin: 0;
  }
  .contact .role {
    font-size: 17px;
    margin: 4px 0 34px;
  }
  .contact .address {
    font-size: 18px;
    line-height: 1.3;
    margin: 0 0 4px;
  }
  .contact ul {
    list-style: none;
    margin: 0;
    padding: 0;
    font-size: 18px;
  }
  .contact li {
    display: flex;
    align-items: center;
    height: 26px;
  }
  .contact li .icon {
    width: 20px;
    height: 16px;
    margin-right: 16px;
    flex: none;
  }
  .contact li.no-icon { padding-left: 36px; }
  .contact .web-group { margin-top: 18px; }

  .brand {
    position: absolute;
    right: 50px;
    top: 200px;
    text-align: center;
  }
  .brand .mark {
    display: flex;
    align-items: center;
    gap: 12px;
    justify-content: center;
  }
  .brand .dot {
    width: 22px; height: 22px;
    border-radius: 50%;
    background: var(--orange);
  }
  .brand .wordmark {
    font-weight: 700;
    font-size: 34px;
    color: var(--navy);
    margin: 0;
  }
  .brand .tagline {
    margin: 8px 0 0;
    font-size: 10.5px;
    letter-spacing: 0.5px;
    color: var(--orange);
    font-weight: 700;
  }
</style>
</head>
<body>
  <div class="card">
    <div class="top-band"><div class="accent"></div><div class="base"></div></div>

    <div class="contact">
      <p class="name">Joan Ferris</p>
      <p class="role">Executive &amp; Clinical Director</p>
      <p class="address">7183 Marbrook Avenue<br>St. Louis, MO 63902</p>
      <ul>
        <li class="no-icon">314-555-0172</li>
        <li>
          <svg class="icon" viewBox="0 0 20 16" aria-hidden="true"><path d="M5 2h3l1 3-2 1.5c1 2 2.5 3.5 4.5 4.5L13 9l3 1v3c0 1-1 1.5-2 1.5C8 14 3 9 3 4c0-1 .8-2 2-2z" fill="var(--ink)"/></svg>
          314-555-0134
        </li>
        <li>
          <svg class="icon" viewBox="0 0 20 16" aria-hidden="true"><rect x="3" y="5" width="14" height="9" rx="1" fill="var(--ink)"/><rect x="6" y="1" width="8" height="5" fill="none" stroke="var(--ink)" stroke-width="1.5"/></svg>
          314-555-0161
        </li>
      </ul>
      <ul class="web-group">
        <li>
          <svg class="icon" viewBox="0 0 20 16" aria-hidden="true"><rect x="2" y="3" width="16" height="11" fill="none" stroke="var(--ink)" stroke-width="1.6"/><path d="M2 3l8 6 8-6" fill="none" stroke="var(--ink)" stroke-width="1.6"/></svg>
          jferris@brightharborcare.example
        </li>
        <li>
          <svg class="icon" viewBox="0 0 20 16" aria-hidden="true"><circle cx="10" cy="8" r="3" fill="none" stroke="var(--ink)" stroke-width="1.8"/><path d="M13 5v4c0 2 3 2 3-1a6 6 0 1 0-2.5 5" fill="none" stroke="var(--ink)" stroke-width="1.8"/></svg>
          www.brightharborcare.example
        </li>
      </ul>
    </div>

    <div class="brand">
      <div class="mark">
        <span class="dot"></span>
        <p class="wordmark">BrightHarbor, LLC</p>
      </div>
      <p class="tagline">WE BRING QUALITY CARE RIGHT TO YOUR HOME</p>
    </div>
  </div>
</body>
</html>
```